Flyer for a Business Consultant

I need a one-page description of services. I am a Brennick Certifed Talents Mentor. I do not have a personal website but think I will soon purchase this template https://varlowskins.example/skins/lectern/. I like the larger font, simplicity and larger font. I will attach his pricing flyer which I like - not to overly guide or restrict your creative thinking, but only to give a little perspective. I don't like busy, noisy - I like clarity, simplicity. Here 's the Brennick website which these same traits https://www.brennicktalentshub.example/ and can be a source of ideas and colors.

Target Market(s)

CEOs and Middle Managers in organizations

Industry/Entity Type

Financial Service

Colors

Designer to choose colors to be used in the design.

Requirements
Must have
• Clarity, simplicity, but also strength (not weak or frilly looking)
Nice to have
• Warm color(s), larger/not skinny font
Should not have
• Loud, noisy, busy

```html
<!DOCTYPE html>
<html lang="en">
<head>
<meta charset="utf-8">
<title>Team Effectiveness Flyer</title>
<link href="https://fonts.googleapis.com/css2?family=PT+Sans:wght@400;700&family=PT+Sans+Narrow:wght@400;700&display=swap" rel="stylesheet">
<style>
  :root {
    --page-bg: #e4e4e6;
    --navy: #0f1822;
    --ink: #1b222b;
    --white: #ffffff;
    --col-light: #c1bbba;
    --col-mid: #958e8d;
    --col-dark: #716a69;
    --footer: #e8efc0;
    --badge: #7d8a62;
    --footer-text: #5e5b57;
    --rule: #cfcfcf;
  }
  * { margin: 0; padding: 0; box-sizing: border-box; }
  html, body { width: 1200px; height: 1200px; overflow: hidden; background: var(--page-bg); }
  .flyer {
    position: absolute; left: 151px; top: 20px;
    width: 927px; height: 1198px;
    transform: scale(0.968); transform-origin: top left;
    background: var(--white);
    font-family: "PT Sans Narrow", "Arial Narrow", sans-serif;
    color: var(--ink);
    overflow: hidden;
  }
  .hero-photo {
    position: absolute; left: 0; top: 0; width: 927px; height: 778px;
    background:
      linear-gradient(180deg, rgba(255,255,255,0) 0%, rgba(255,255,255,0) 62%, rgba(255,255,255,.85) 84%, #fff 100%),
      radial-gradient(ellipse 55% 30% at 50% 58%, #e9ddd4 0%, rgba(233,221,212,0) 100%),
      linear-gradient(180deg, #0f1822 0%, #131c26 30%, #5a4a44 44%, #a98472 56%, #c9a492 66%, #e6dcd6 80%, #ffffff 100%);
  }
  .headline { position: absolute; left: 0; width: 100%; text-align: center; color: var(--white); font-family: "PT Sans", sans-serif; font-weight: 400; }
  .headline-kicker { top: 84px; font-size: 44px; letter-spacing: 0.5px; }
  .headline-main { top: 142px; font-size: 62px; letter-spacing: 0.5px; }
  .promise { position: absolute; left: 0; width: 100%; text-align: center; font-family: "PT Sans", sans-serif; color: var(--ink); font-size: 42px; line-height: 50px; top: 560px; }
  .benefits { position: absolute; left: 0; width: 100%; top: 670px; list-style: none; text-align: center; font-size: 17.5px; }
  .benefits li { height: 30px; line-height: 28px; }
  .benefits li + li { border-top: 1px solid var(--rule); margin: 0 140px; }
  .services { position: absolute; left: 0; top: 778px; width: 927px; height: 290px; display: flex; gap: 2px; background: var(--white); }
  .service { flex: 1; color: var(--white); padding: 17px 34px 0 43px; }
  .service--sessions { background: var(--col-light); }
  .service--workshop { background: var(--col-mid); padding-left: 30px; }
  .service--modules { background: var(--col-dark); padding-left: 41px; }
  .service-title { font-family: "PT Sans", sans-serif; font-weight: 400; font-size: 25px; line-height: 28px; }
  .service-sub { font-size: 13.5px; line-height: 14px; text-transform: uppercase; }
  .service-body { margin-top: 20px; font-size: 15.5px; line-height: 20px; text-align: justify; hyphens: auto; }
  .contact-bar { position: absolute; left: 0; top: 1068px; width: 927px; height: 130px; background: var(--footer); }
  .cert { position: absolute; left: 44px; top: 24px; display: flex; align-items: center; gap: 12px; color: var(--badge); }
  .cert-square { width: 48px; height: 58px; background: var(--badge); }
  .cert-name { font-size: 15px; line-height: 20px; }
  .cert-name span { display: block; font-size: 25px; line-height: 26px; }
  .portrait { position: absolute; left: 309px; top: 8px; width: 96px; height: 96px; border-radius: 50%;
    background: radial-gradient(circle at 50% 40%, #d7a58f 0%, #8c5a45 45%, #3a2a26 100%); }
  .coach { position: absolute; left: 415px; top: 28px; color: var(--footer-text); }
  .coach-name { font-size: 27px; line-height: 30px; }
  .coach-role { font-size: 13px; }
  .contact { position: absolute; left: 660px; top: 30px; list-style: none; color: var(--footer-text); font-size: 18px; }
  .contact li { display: flex; align-items: center; gap: 12px; height: 26px; }
  .contact .phone { font-family: "PT Sans", sans-serif; font-weight: 700; letter-spacing: 3px; font-size: 18px; }
  .contact svg { width: 16px; height: 16px; fill: var(--footer-text); }
</style>
</head>
<body>
  <main class="flyer">
    <div class="hero-photo" role="img" aria-label="Photo of team members' hands joined in a circle of fist bumps"></div>
    <h1>
      <span class="headline headline-kicker">A STRENGTH-BASED APPROACH TO</span>
      <span class="headline headline-main">MANAGING TEAM EFFECTIVENESS</span>
    </h1>
    <h2 class="promise">WE HELP<br>TEAMS GROW STRONGER BY</h2>
    <ul class="benefits">
      <li>Bringing a deep awareness of their strengths and the strengths of their associates.</li>
      <li>Increasing the Team’s communication and sense of partnership.</li>
      <li>Improving employee engagement and effectiveness.</li>
    </ul>

    <section class="services">
      <article class="service service--sessions">
        <h3 class="service-title">INDIVIDUAL</h3>
        <p class="service-sub">Sessions</p>
        <p class="service-body">Conversational feedback and coaching sessions based on Brennick’s TalentPrint assessments. These sessions last about an hour and lead to a personalized translation of the results and how their strengths show up in their work and inherent blind spots they bring.</p>
      </article>
      <article class="service service--workshop">
        <h3 class="service-title">STRENGTH DISCOVERY</h3>
        <p class="service-sub">Workshop</p>
        <p class="service-body">A retreat-style Team Workshop in which the team learns each other’s unique Top 5 strengths. The session is very interactive and provides a common language that leads to improved communication and effectiveness. Tailored in 2.3.and 4-hour options are tailored to your Team’s challenges and opportunities.</p>
      </article>
      <article class="service service--modules">
        <h3 class="service-title">FOLLOW-ON</h3>
        <p class="service-sub">Modules</p>
        <p class="service-body">Follow-on is important to make the insights learned to be practical and integrated into the Teams’ approach and workflows. In a debrief session included as part of the workshop, we provide several 15-minute exercise modules for use in regular meetings, and we offer guest facilitated modules of 30- 60 minutes each.</p>
      </article>
    </section>

    <footer class="contact-bar">
      <div class="cert">
        <div class="cert-square"></div>
        <p class="cert-name">BRENNICK CERTIFIED<span>Talents Mentor</span></p>
      </div>
      <div class="portrait" role="img" aria-label="Portrait photo of the coach"></div>
      <div class="coach">
        <p class="coach-name">Warren Delacourt</p>
        <p class="coach-role">Brennick Workplace Talents Mentor</p>
      </div>
      <ul class="contact">
        <li>
          <svg viewBox="0 0 16 16" aria-hidden="true"><path d="M8 1a7 7 0 1 0 3.5 13.1l-.6-1.1A5.8 5.8 0 1 1 13.8 8v.9c0 .8-.5 1.3-1.1 1.3s-1-.5-1-1.3V4.6h-1.2v.6A3.3 3.3 0 1 0 10.7 10a2.2 2.2 0 0 0 2 1.3c1.3 0 2.3-1 2.3-2.5V8A7 7 0 0 0 8 1Zm0 9.2A2.2 2.2 0 1 1 8 5.8a2.2 2.2 0 0 1 0 4.4Z"/></svg>
          <span>warren@talentsfocus.example</span>
        </li>
        <li>
          <svg viewBox="0 0 16 16" aria-hidden="true"><path d="M5 1 3 2c-1 2-1 7 2 12l2 1 1-1-1.6-3.4-1.6.6C4 9 4 6.5 4.6 5l1.7.3L7 1.6Z"/></svg>
          <span class="phone">555-014-2277</span>
        </li>
      </ul>
    </footer>
  </main>
</body>
</html>
```